Business Card Design

I need a business card designed for my new company BrightOak Home developments I specialise in all aspects of carpentry including Decks, Pergolas, Conventional Framing and fit outs I am open to different colours as long as it fits with my logo.

Industry/Entity Type

Carpentry

Contact Information for Business Card

BrightOak Home Developments, Rob Keltmore, 0481604328, specialising in all aspects of carpentry and construction

```html
<!DOCTYPE html>
<html lang="en">
<head>
<meta charset="utf-8">
<title>BrightOak Home Developments – Business Card</title>
<link rel="stylesheet" href="https://fonts.googleapis.com/css2?family=Josefin+Sans:wght@300;400&display=swap">
<style>
  :root {
    --brand-blue: #3463b8;
    --brand-orange: #ef7a26;
    --card-white: #ffffff;
    --backdrop: #e9e6e1;
    --ink-blue: #2f5cae;
    --card-shadow: rgba(0, 0, 0, 0.18);
  }
  * { box-sizing: border-box; margin: 0; padding: 0; }
  html, body {
    width: 1200px;
    height: 873px;
    overflow: hidden;
    background: var(--backdrop);
    font-family: "Josefin Sans", sans-serif;
  }
  .sheet {
    position: relative;
    width: 1200px;
    height: 873px;
    display: flex;
    align-items: center;
    justify-content: center;
    gap: 60px;
  }
  .card {
    position: relative;
    width: 520px;
    height: 297px;
    background: var(--card-white);
    box-shadow: 0 6px 18px var(--card-shadow);
    overflow: hidden;
    color: var(--ink-blue);
  }
  .card__top-band {
    position: absolute;
    left: 0; right: 0; top: 0;
    height: 22px;
    background: var(--brand-blue);
  }
  .card__stripes {
    position: absolute;
    left: 0; right: 0; bottom: 0;
    display: flex;
    flex-direction: column;
  }
  .stripe { width: 100%; }
  .stripe--blue-thin { height: 6px; background: var(--brand-blue); }
  .stripe--gap { height: 4px; background: var(--card-white); }
  .stripe--orange { height: 8px; background: var(--brand-orange); }
  .stripe--blue-edge { height: 11px; background: var(--brand-blue); }

  /* Brand name lockup */
  .brand {
    display: flex;
    align-items: center;
    gap: 8px;
    color: var(--ink-blue);
    font-weight: 300;
    text-transform: uppercase;
  }
  .brand__square {
    flex: none;
    border: 1.5px solid var(--ink-blue);
  }
  .brand__text { display: flex; flex-direction: column; line-height: 1; }

  .card--front .brand {
    position: absolute;
    left: 34px;
    top: 54px;
  }
  .card--front .brand__square { width: 14px; height: 14px; }
  .card--front .brand__name { font-size: 22px; letter-spacing: 0.5px; }
  .card--front .brand__sub { font-size: 10px; letter-spacing: 1.4px; margin-top: 4px; }

  .card--back .brand {
    position: absolute;
    left: 50%;
    top: 50%;
    transform: translate(-50%, -58%);
    gap: 14px;
  }
  .card--back .brand__square { width: 30px; height: 30px; border-width: 2px; }
  .card--back .brand__name { font-size: 46px; letter-spacing: 1px; }
  .card--back .brand__sub { font-size: 20px; letter-spacing: 3px; margin-top: 6px; }

  /* Contact block */
  .contact {
    position: absolute;
    left: 250px;
    top: 92px;
    width: 240px;
    font-weight: 300;
    text-transform: uppercase;
    color: var(--ink-blue);
  }
  .contact__marker {
    position: absolute;
    left: -22px;
    top: -10px;
  }
  .contact__line {
    display: block;
    padding: 6px 0 5px 0;
    border-bottom: 2px solid var(--brand-orange);
  }
  .contact__name { font-size: 17px; letter-spacing: 0.6px; }
  .contact__phone { font-size: 16px; letter-spacing: 0.6px; }
  .contact__tagline {
    font-size: 12.5px;
    line-height: 1.3;
    letter-spacing: 0.4px;
    padding-top: 7px;
  }
</style>
</head>
<body>
  <main class="sheet">
    <!-- Front: contact side -->
    <section class="card card--front" aria-label="Business card front">
      <div class="card__top-band"></div>

      <div class="brand">
        <span class="brand__square" aria-hidden="true"></span>
        <span class="brand__text">
          <span class="brand__name">BrightOak</span>
          <span class="brand__sub">Home Developments</span>
        </span>
      </div>

      <div class="contact">
        <svg class="contact__marker" width="12" height="150" viewBox="0 0 12 150" aria-hidden="true">
          <polygon points="2,0 12,0 8,150 6,150" fill="var(--brand-blue)"/>
        </svg>
        <span class="contact__line contact__name">Rob Keltmore</span>
        <span class="contact__line contact__phone">0481604328</span>
        <span class="contact__line contact__tagline">Specialising in all aspects<br>of carpentry<br>and construction</span>
      </div>

      <div class="card__stripes" aria-hidden="true">
        <div class="stripe stripe--blue-thin"></div>
        <div class="stripe stripe--gap"></div>
        <div class="stripe stripe--orange"></div>
        <div class="stripe stripe--gap"></div>
        <div class="stripe stripe--blue-edge"></div>
      </div>
    </section>

    <!-- Back: brand side -->
    <section class="card card--back" aria-label="Business card back">
      <div class="card__top-band"></div>

      <div class="brand">
        <span class="brand__square" aria-hidden="true"></span>
        <span class="brand__text">
          <span class="brand__name">BrightOak</span>
          <span class="brand__sub">Home Developments</span>
        </span>
      </div>

      <div class="card__stripes" aria-hidden="true">
        <div class="stripe stripe--blue-thin"></div>
        <div class="stripe stripe--gap"></div>
        <div class="stripe stripe--orange"></div>
        <div class="stripe stripe--gap"></div>
        <div class="stripe stripe--blue-edge"></div>
      </div>
    </section>
  </main>
</body>
</html>
```